Wordpress Theme: Love and Relationships

We need a theme for a Wordpress site about:

LOVE AND RELATIONSHIP TOPICS

General Design & Layout
- Simple but unique logo (Wordmark / Pictorial / Combination / Emblem / Character)
- Drop down header navigation with 3 layers / levels (Category -> Sub category -> Sub sub category)
- Valid HTML5
- Content area with white (or other single bright color) background only, no background images or gradients allowed

THIS SHOULD INCLUDE THE THEME CODING, SEE MORE INFO BELOW!

Reason: I'll be on vacation, so I'd rather extend the deadline.

Requirements
Must have
• Details
- Headlines on list pages always link to article
- No "read more" buttons
- No "Login" buttons
- No social buttons within teasers on homepage and list pages

Sidebar
- 250px or 300px inner width (for ads)
- No H1-H6 tags for widget titles

Wordpress Theme
- No additional plugins required (like Quarry Framework, Social plugins...)
- Compatible with the latest version of Wordpress (3.5)

Required content elements (please add examples to preview)
- Comments on single / post
- Images (left/right/center/with description & without)
- Text formatting: Bold, underline, lists, headlines (H1-H6), links

Required templates
- Homepage
- Sidebar
- Header
- Footer
- Category
- Single
- Page
- Comments
- Search results

Browser compatibility
- Firefox (>=12)
- Internet Explorer (>=8)
- Chrome (>=20)

```html
<!DOCTYPE html>
<html lang="en">
<head>
<meta charset="utf-8">
<title>Kindred Hours – Blog</title>
<link href="https://fonts.googleapis.com/css2?family=Oswald:wght@300;400&family=PT+Sans:wght@400;700&display=swap" rel="stylesheet">
<style>
:root{
  --red-dark:#5e0c10;
  --red:#8e1a1c;
  --bar:#1b2c33;
  --menu:#23292e;
  --menu-line:#30373c;
  --lime:#c2d82c;
  --orange:#f0a020;
  --teal:#3a7574;
  --sidebar:#e7e7e7;
  --page:#f7f7f7;
  --ink:#333;
  --heading:#2c3e45;
}
*{margin:0;padding:0;box-sizing:border-box}
html,body{width:1190px;height:1200px;overflow:hidden;background:#fff}
.canvas{position:absolute;left:0;top:0;width:1200px;height:1210px;transform:scale(.9917);transform-origin:0 0;font-family:"PT Sans",sans-serif;color:var(--ink);background:#fff;border-left:1px solid var(--red-dark)}
.abs{position:absolute}
.header{left:0;top:0;width:1200px;height:146px;background:radial-gradient(ellipse at 50% 0%,#961c1e 0%,#7c1417 60%,#5d0d10 100%)}
.brand{left:358px;top:38px;display:flex;align-items:center;gap:10px}
.brand-dot{width:18px;height:18px;border-radius:50%;background:var(--orange)}
.brand-name{font-size:28px;font-weight:700;color:#fff;letter-spacing:.5px}
.nav{left:578px;top:37px;display:flex;gap:15px;font-size:12px;color:#fff;align-items:center}
.nav a{color:#fff;text-decoration:none;padding-bottom:3px}
.nav a.active{border-bottom:2px solid var(--lime)}
.social{display:flex;gap:8px;margin-left:0}
.social span{width:10px;height:10px;border-radius:50%;background:var(--lime);display:block}
.titlebar{left:0;top:145px;width:1200px;height:41px;background:linear-gradient(#22353c,#152329);border-top:1px solid #0e1a1e}
.page-title{left:359px;top:152px;font-family:"Oswald",sans-serif;font-size:21px;color:var(--lime);letter-spacing:-.3px}
.search{left:814px;top:155px;width:24px;height:22px;border-radius:11px;background:#121e22}
.search svg{position:absolute;left:7px;top:6px}
.dropdown{width:122px;background:var(--menu);border-radius:4px;box-shadow:0 2px 4px rgba(0,0,0,.4);font-size:9px;color:#ddd;padding-top:0}
.dropdown li{list-style:none;height:21px;line-height:21px;padding-left:13px;border-bottom:1px solid var(--menu-line)}
.dropdown li:last-child{border-bottom:0}
.dropdown li.current{font-weight:700;color:#fff;background:#1b2024;border-bottom:2px solid var(--lime)}
.dd-one{left:567px;top:60px}
.dd-two{left:690px;top:81px}
.main-bg{left:0;top:186px;width:840px;height:977px;background:#fff}
.page-bg{left:358px;top:186px;width:322px;height:977px;background:var(--page)}
.sidebar-bg{left:680px;top:186px;width:160px;height:977px;background:var(--sidebar)}
.post{left:359px;width:311px;height:277px;background:#fff;box-shadow:0 1px 3px rgba(0,0,0,.35)}
.post-head{padding:16px 0 0 19px;height:62px;font-family:"Oswald",sans-serif;font-weight:300;line-height:16px}
.post-title{font-size:14px;color:#222}
.post-meta{font-size:13px;color:var(--lime)}
.post-image{height:100px;background:var(--teal)}
.post-body{padding:13px 17px 0 17px;font-size:7.4px;line-height:12px;color:#444}
.post-more{text-align:right;padding:11px 23px 0 0;font-size:9px;color:#222}
.post-more b{color:var(--lime);font-weight:400}
.widget{left:699px;width:124px;border-bottom:2px solid var(--orange);padding-bottom:6px}
.widget-title{font-size:15px;font-weight:700;color:var(--heading);letter-spacing:-.4px;margin-bottom:2px}
.widget ul{list-style:none;font-size:10px;color:#444;line-height:12px}
.widget li::before{content:"";display:inline-block;border-left:5px solid #555;border-top:3px solid transparent;border-bottom:3px solid transparent;margin:0 5px 0 1px}
.ad{left:698px;top:495px;width:125px;height:125px;background:var(--teal);color:#fff;font-family:"Oswald",sans-serif;font-weight:300;font-size:21px;display:flex;align-items:center;justify-content:center;letter-spacing:-.5px}
.pager{left:576px;top:1107px;display:flex;gap:4px}
.pager span{width:20px;height:20px;background:#fff;font-size:9px;text-align:center;line-height:20px;color:#222}
.pager .arrow{color:var(--lime);font-size:12px}
.pager .muted{color:#ccc}
.footer{left:0;top:1163px;width:1200px;height:47px;background:linear-gradient(#6a0e12,#4e090c)}
.footer-nav{left:358px;top:1176px;display:flex;gap:10px;font-size:8px;color:#fff}
.footer-nav .active{color:var(--lime)}
</style>
</head>
<body>
<div class="canvas">
  <header class="abs header"></header>
  <div class="abs brand"><span class="brand-dot"></span><span class="brand-name">Kindred Hours</span></div>
  <nav class="abs nav">
    <a class="active">Home</a><a>About</a><a>Blog</a><a>Products</a><a>Page Templates</a>
    <div class="social"><span></span><span></span><span></span></div>
  </nav>

  <div class="abs titlebar"></div>
  <h1 class="abs page-title">WELCOME TO OUR BLOG</h1>
  <div class="abs search"><svg width="10" height="10" viewBox="0 0 10 10"><circle cx="6" cy="4" r="2.6" fill="none" stroke="#fff" stroke-width="1.3"/><line x1="4.1" y1="5.9" x2="1.5" y2="8.5" stroke="#fff" stroke-width="1.4"/></svg></div>

  <div class="abs main-bg"></div>
  <div class="abs page-bg"></div>
  <div class="abs sidebar-bg"></div>

  <ul class="abs dropdown dd-one">
    <li>Home</li><li class="current">About Us</li><li>Link Goes Here</li><li>This Is Something</li><li>Click This URL</li><li>Sitemap</li>
  </ul>

  <article class="abs post" style="top:208px">
    <div class="post-head"><div class="post-title">POST TITLE GOES HERE</div><div class="post-meta">POSTED BY ADMIN ON JUNE 7 IN SOME CATEGORY</div></div>
    <div class="post-image" role="img" aria-label="Featured image for the post"></div>
    <p class="post-body">Nunc turpis neque, feugiat eget eleifend et, lacinia non neque. Praesent rhoncus ultrices posuere. Pellentesque vel lacus eget nisi convallis auctor. Nam vitae lectus eu libero pellentesque pulvinar urna risus, mattis pulvinar bibendum in, venenatis quis neque. Mauris nec metus ultricies erat consequat dignissim non eu nisl. Quisque libero tellus, pharetra et eleifend id, interdum elementum arcu. Suspendisse quis</p>
    <p class="post-more">Continue <b>»</b></p>
  </article>
  <article class="abs post" style="top:512px">
    <div class="post-head"><div class="post-title">POST TITLE GOES HERE</div><div class="post-meta">POSTED BY ADMIN ON JUNE 7 IN SOME CATEGORY</div></div>
    <div class="post-image" role="img" aria-label="Featured image for the post"></div>
    <p class="post-body">Nunc turpis neque, feugiat eget eleifend et, lacinia non neque. Praesent rhoncus ultrices posuere. Pellentesque vel lacus eget nisi convallis auctor. Nam vitae lectus eu libero pellentesque pulvinar urna risus, mattis pulvinar bibendum in, venenatis quis neque. Mauris nec metus ultricies erat consequat dignissim non eu nisl. Quisque libero tellus, pharetra et eleifend id, interdum elementum arcu. Suspendisse quis</p>
    <p class="post-more">Continue <b>»</b></p>
  </article>
  <article class="abs post" style="top:815px">
    <div class="post-head"><div class="post-title">POST TITLE GOES HERE</div><div class="post-meta">POSTED BY ADMIN ON JUNE 7 IN SOME CATEGORY</div></div>
    <div class="post-image" role="img" aria-label="Featured image for the post"></div>
    <p class="post-body">Nunc turpis neque, feugiat eget eleifend et, lacinia non neque. Praesent rhoncus ultrices posuere. Pellentesque vel lacus eget nisi convallis auctor. Nam vitae lectus eu libero pellentesque pulvinar urna risus, mattis pulvinar bibendum in, venenatis quis neque. Mauris nec metus ultricies erat consequat dignissim non eu nisl. Quisque libero tellus, pharetra et eleifend id, interdum elementum arcu. Suspendisse quis</p>
    <p class="post-more">Continue <b>»</b></p>
  </article>

  <div class="abs pager"><span class="arrow">«</span><span class="muted">1</span><span>2</span><span class="arrow">»</span></div>

  <aside>
    <div class="abs widget" style="top:205px">
      <div class="widget-title">Recent Posts :</div>
      <ul><li>Simply dummy text</li><li>Simple test dummy</li><li>Lorem Ipsum Simply</li><li>Simply dummy text</li><li>Simple test dummy</li></ul>
    </div>
    <div class="abs widget" style="top:292px">
      <div class="widget-title">Category :</div>
      <ul><li>Test 1 category</li><li>Test 2 category</li><li>Test 3 category</li><li>Test 4 category</li><li>Test 5 category</li></ul>
    </div>
    <div class="abs widget" style="top:385px">
      <div class="widget-title">Archives :</div>
      <ul><li>June 2013</li><li>May 2013</li><li>April 2013</li><li>March 2013</li></ul>
    </div>
    <div class="abs ad">Advertisement</div>
  </aside>

  <ul class="abs dropdown dd-two">
    <li>Home</li><li class="current">About Us</li><li>Link Goes Here</li><li>This Is Something</li><li>Click This URL</li><li>Sitemap</li>
  </ul>

  <footer class="abs footer"></footer>
  <nav class="abs footer-nav"><span class="active">Home</span><span>About</span><span>Blog</span><span>Products</span><span>Page Templates</span><span>Shortcodes</span></nav>
</div>
</body>
</html>
```